Entertainer/Dancer Business Cards

Corwin Latimer is an up and coming entertainer from Baltimore, Maryland currently relocating to Los Angeles, California for a dance opportunity at the renowned Marnie Holt Movement Loft.
This young man needs to promote himself and his skills in a populous and competitive city.
Hopefully, this card will set him apart from the tons of entertainers in L.A.
It will passed out to fellow entertainers, agents, and random people looking for talent.

I have uploaded an image of the dancer, it is not necessary to use this image; however it is in PSD format if one should decide to incorporate it somehow and would like to make changes.

Industry/Entity Type

Business

Contact Information for Business Card

Corwin Latimer
(line 1) Dancer Choreographer Instructor Singer/Songwriter
(line 2) Ballet-Modern-Urban
corwinlatimer00@quillpost.example
410-582-7146

Requirements
Nice to have

• Open to an all typography card.
Should not have
• No logo; just name: Corwin Latimer
Corwin is a guy (in case you were wondering :D )
Please no ballet/pointe shoes in design

```html
<!DOCTYPE html>
<html lang="en">
<head>
<meta charset="utf-8">
<title>Corwin Latimer — Business Card</title>
<link rel="stylesheet" href="https://fonts.googleapis.com/css2?family=Arimo:wght@400;700&display=swap">
<style>
  :root {
    --page-bg: #e8edf4;
    --card-navy: #243d63;
    --band-green: #6ab777;
    --band-teal: #5a8aa2;
    --portrait-light: #4a6fa8;
    --portrait-dark: #34578f;
  }
  html, body {
    margin: 0;
    width: 1200px;
    height: 1000px;
    overflow: hidden;
    background: var(--page-bg);
  }
  .card {
    position: absolute;
    left: 240px;
    top: 288px;
    width: 700px;
    height: 410px;
    background: var(--card-navy);
    overflow: hidden;
  }
  .card svg { display: block; }
  .card-text {
    font-family: "Arimo", Arial, sans-serif;
    fill: var(--card-navy);
  }
  .name { font-size: 30px; font-weight: 700; }
  .roles { font-size: 15px; font-weight: 400; }
  .styles { font-size: 15px; font-weight: 400; }
  .email { font-size: 18px; font-weight: 400; }
  .phone { font-size: 18px; font-weight: 400; }
</style>
</head>
<body>
  <div class="card">
    <svg width="700" height="410" viewBox="0 0 700 410" xmlns="http://www.w3.org/2000/svg">
      <defs>
        <linearGradient id="band-gradient" x1="0" y1="0" x2="0" y2="1">
          <stop offset="0" stop-color="var(--band-green)"/>
          <stop offset="1" stop-color="var(--band-teal)"/>
        </linearGradient>
        <linearGradient id="portrait-gradient" x1="0" y1="0" x2="0" y2="1">
          <stop offset="0" stop-color="var(--portrait-light)"/>
          <stop offset="1" stop-color="var(--portrait-dark)"/>
        </linearGradient>
      </defs>

      <polygon class="diagonal-band" points="453,0 700,0 700,90 257,410 0,410 0,327" fill="url(#band-gradient)"/>

      <circle class="portrait-ring" cx="170" cy="144" r="108" fill="var(--card-navy)"/>
      <circle class="portrait" cx="170" cy="144" r="98" fill="url(#portrait-gradient)"
              role="img" aria-label="Portrait photo of the dancer"/>

      <g class="card-text">
        <text class="name" transform="translate(300,194) rotate(-35.9)">Corwin Latimer</text>
        <line class="name-rule" x1="312" y1="199" x2="488" y2="77" stroke="var(--card-navy)" stroke-width="1"/>
        <text class="roles" transform="translate(208,309) rotate(-35.9)">Dancer Choreographer Instructor Singer/Songwriter</text>
        <text class="styles" transform="translate(220,327) rotate(-35.9)">Ballet-Modern-Urban</text>
        <text class="email" transform="translate(234,347) rotate(-35.9)">corwinlatimer00@quillpost.example</text>
        <text class="phone" transform="translate(250,368) rotate(-35.9)">410-582-7146</text>
      </g>
    </svg>
  </div>
</body>
</html>
```